Simple and clean webdesign for personal homepage

Trying to create a simple and clean webdesign for my personal homepage. Going to use a static site builder with templates to build the site. I want it to have multiple pages - like an about me, blog and resume. I just need something very basic I can customize. I want the main colors to be purple, black and white. I am open to other color palettes too but since purple is my favorite color I want that to be one of the main colors.

The site be mostly text driven. Might have some images in the body text but I want the site design to be light and lean.

Industry/Entity Type

Personal Homepage.

Coding

Coded - Design and coding required

Number of Pages Required

1 page

Font styles to use
Sans Serif

Colors
6B429C
8869AF
B7A5CE
E3DAEB
F3F0F8

Requirements
Must have
• Clean design. Purple used as a color. HTML template.
Nice to have
• Responsive

```html
<!DOCTYPE html>
<html lang="en">
<head>
<meta charset="utf-8">
<title>Nadia Verell — Personal Homepage</title>
<link href="https://fonts.googleapis.com/css2?family=Varela+Round&family=Open+Sans:wght@400;600;700&display=swap" rel="stylesheet">
<style>
:root{
  --purple:#6B429C;
  --purple-mid:#8869AF;
  --lilac:#B7A5CE;
  --lilac-soft:#E3DAEB;
  --mist:#F3F0F8;
  --blue:#6C8BE0;
  --ink:#2a2a2a;
  --text:#6d6d6d;
  --muted:#9a9a9a;
  --footer:#272a3d;
  --footer-text:#9ea0b3;
  --orange:#F7931E;
  --white:#ffffff;
}
*{box-sizing:border-box;margin:0;padding:0}
html,body{width:1200px;height:5062px;overflow:hidden}
body{position:relative;background:var(--white);font-family:'Open Sans',sans-serif;color:var(--text)}
.abs{position:absolute}
.display{font-family:'Varela Round',sans-serif;font-weight:400;color:var(--ink)}
.btn{position:absolute;display:flex;align-items:center;justify-content:space-between;padding:0 24px;font-size:13px;font-weight:600;border-radius:2px}
.btn svg{width:26px;height:10px}
.btn-purple{background:var(--purple);color:var(--white)}
.btn-white{background:var(--white);color:var(--purple)}
.btn-soft{background:var(--mist);color:var(--purple);border:1px solid var(--lilac-soft)}
.photo{position:absolute}

/* hero */
.hero{position:absolute;left:0;top:0;width:1200px;height:683px;background:var(--purple);overflow:hidden}
.logo{position:absolute;font-family:'Varela Round',sans-serif;font-size:31px;color:var(--white)}
.nav a{position:absolute;top:36px;color:var(--white);font-size:13px;font-weight:600;text-decoration:none}
.nav-cta{position:absolute;left:913px;top:20px;width:171px;height:49px;border:2px solid rgba(255,255,255,.8);color:var(--white);display:flex;align-items:center;justify-content:space-between;padding:0 18px;font-size:14px;font-weight:600}
.hero-bar{left:118px;top:236px;width:6px;height:104px;background:var(--white)}
.hero-kicker{left:148px;top:232px;font-size:31px;font-weight:700;color:var(--white);letter-spacing:1px}
.hero-name{left:145px;top:262px;font-size:80px;color:var(--white)}
.hero-lead{left:114px;top:378px;width:500px;font-size:18px;line-height:31px;font-weight:600;color:var(--white)}
.social-rail span{position:absolute;left:1130px;font-size:10px;letter-spacing:2px;color:rgba(255,255,255,.7);transform:rotate(-90deg);transform-origin:left top;font-weight:600}
.chat-badge{left:1058px;top:655px;width:60px;height:60px;border-radius:50%;background:var(--orange);display:flex;align-items:center;justify-content:center;box-shadow:0 6px 16px rgba(247,147,30,.35)}

/* interests */
.sec-title{font-size:46px}
.body-copy{font-size:15px;line-height:28px;color:var(--text)}
.stat-num{font-family:'Varela Round',sans-serif;font-size:64px;color:var(--purple);line-height:1}
.stat-label{font-size:15px;line-height:21px;color:var(--text)}
.band{left:0;top:1375px;width:1200px;height:874px;background:var(--mist)}
.service{position:absolute;top:1224px;width:304px;height:318px;background:var(--white);box-shadow:0 8px 24px rgba(107,66,156,.08);padding:150px 0 0 112px}
.service svg{position:absolute;left:32px;top:156px;width:52px;height:52px}
.service h3{font-family:'Varela Round',sans-serif;font-weight:400;font-size:34px;line-height:41px;color:var(--ink)}
.service p{margin-top:18px;font-size:13px;color:var(--muted)}
.service.active{background:var(--blue)}
.service.active h3,.service.active p{color:var(--white)}

/* projects */
.project{position:absolute}
.project .shot{position:absolute;left:0;top:0;width:100%;box-shadow:0 6px 20px rgba(0,0,0,.1)}
.project-name{position:absolute;font-family:'Varela Round',sans-serif;font-size:24px;color:var(--ink);white-space:nowrap}
.slider-track{left:273px;top:3114px;width:621px;height:2px;background:#e6e6e6}
.slider-fill{left:273px;top:3113px;width:175px;height:4px;background:var(--blue)}
.slider-arrow{position:absolute;top:3087px;width:47px;height:46px;border:1px solid #e3e3e3;display:flex;align-items:center;justify-content:center}

/* resume */
.resume-bg{left:0;top:3231px;width:1200px;height:723px;background:var(--mist)}
.resume-side{left:0;top:3231px;width:328px;height:723px;background:var(--purple)}
.avatar{left:186px;top:3380px;width:264px;height:264px;border-radius:50%;border:8px solid var(--white);background:radial-gradient(circle at 50% 45%,#4a3a36,#2b9ccf 60%);box-shadow:0 10px 30px rgba(0,0,0,.15)}
.info-label{position:absolute;font-size:11px;font-weight:700;letter-spacing:1.5px;color:var(--ink)}
.info-value{position:absolute;font-size:13px;color:var(--muted)}
.tag{position:absolute;height:24px;padding:0 18px;border:1px solid var(--lilac);border-radius:12px;font-size:11px;line-height:22px;color:var(--text);background:var(--white)}

/* blog */
.blog-date{position:absolute;font-size:11px;letter-spacing:2px;color:var(--muted);font-weight:600}
.blog-title{position:absolute;font-size:19px;line-height:29px;font-weight:600;color:var(--ink)}
.read-more{position:absolute;font-size:12px;font-weight:700;letter-spacing:2px;color:var(--purple);border-bottom:1px solid var(--purple);padding-bottom:2px}
.blog-arrow{position:absolute;top:4290px}

/* footer */
.footer{left:0;top:4647px;width:1200px;height:415px;background:var(--footer)}
.foot-head{position:absolute;font-size:13px;font-weight:700;color:var(--white)}
.foot-link{position:absolute;font-size:13px;color:var(--footer-text)}
.foot-icon{position:absolute;width:24px;height:24px;border-radius:50%;background:#3a3d55;display:flex;align-items:center;justify-content:center}
.newsletter-input{left:835px;top:4828px;width:249px;height:40px;border:1px solid #4a4d66;padding:0 14px;font-size:12px;line-height:38px;color:#6d7088}
.newsletter-btn{left:835px;top:4885px;width:249px;height:38px;background:var(--purple);color:var(--white);font-size:12px;font-weight:700;letter-spacing:1.5px;text-align:center;line-height:38px}
.foot-rule{left:112px;top:5000px;width:972px;height:1px;background:#3a3d55}
.social-dot{position:absolute;top:5018px;width:30px;height:30px;border-radius:50%;background:#3a3d55}
</style>
</head>
<body>

<!-- HERO -->
<header class="hero">
  <div class="logo" style="left:112px;top:22px">Nadia Verell</div>
  <nav class="nav">
    <a style="left:460px">Home</a>
    <a style="left:547px">About</a>
    <a style="left:638px">Portfolio</a>
    <a style="left:746px">Blog</a>
    <a style="left:828px">Resume</a>
  </nav>
  <div class="nav-cta">Get in touch
    <svg width="22" height="10" viewBox="0 0 22 10"><path d="M0 5h20M16 1l4 4-4 4" stroke="#fff" stroke-width="1.6" fill="none"/></svg>
  </div>
  <div class="abs hero-bar"></div>
  <div class="abs hero-kicker">HELLO, I AM</div>
  <div class="abs display hero-name">Nadia Verell</div>
  <p class="abs hero-lead">Porin condimentum ornare. Praesent a neque leo. Suspendisse congue, ligula quis tincidunt bibendum sed ammt dictam.</p>
  <div class="btn btn-white" style="left:114px;top:505px;width:174px;height:47px">Meet Nadia
    <svg viewBox="0 0 26 10"><path d="M2 5h20M18 1l4 4-4 4" stroke="#6B429C" stroke-width="1.6" fill="none"/></svg>
  </div>
  <div class="photo" role="img" aria-label="Portrait photo of a smiling woman in a blue top" style="left:658px;top:40px;width:402px;height:643px;background:linear-gradient(160deg,#5a3a84 0%,#3b2a3a 40%,#2fb6e4 80%,#27a3d6 100%);border-radius:200px 200px 0 0"></div>
  <div class="social-rail">
    <span style="top:215px">PAGEWALL</span>
    <span style="top:322px">WORKNET</span>
    <span style="top:447px">PHOTOLOG</span>
    <span style="top:550px">CHIRPLINE</span>
  </div>
</header>
<div class="abs chat-badge">
  <svg width="26" height="22" viewBox="0 0 26 22"><path d="M2 2h22v14H9l-5 4v-4H2z" fill="none" stroke="#fff" stroke-width="2"/><path d="M7 8h12M7 11h9" stroke="#fff" stroke-width="1.6"/></svg>
</div>

<!-- AREA OF INTERESTS -->
<h2 class="abs display sec-title" style="left:120px;top:842px">Area of interests</h2>
<p class="abs body-copy" style="left:114px;top:926px;width:390px">Porin condimentum ornare. Praesent a neque leo. Suspendisse congue, ligula quis tincidunt bibendum sed.</p>
<div class="btn btn-soft" style="left:114px;top:1047px;width:174px;height:45px">Contact us
  <svg viewBox="0 0 26 10"><path d="M2 5h20M18 1l4 4-4 4" stroke="#6B429C" stroke-width="1.6" fill="none"/></svg>
</div>
<h3 class="abs display" style="left:613px;top:800px;width:460px;font-size:34px;line-height:42px">Etiam consectetur pulvinar lorem a laoreet. Nulla ut volutpat lacus</h3>
<p class="abs" style="left:613px;top:951px;width:430px;font-size:13px;line-height:28px">Interdum et malesuada fames ac ante ipsum primis in faucibus. Donec ut suscipit purus. Praesent feugiat, magna sed ultricies ullamcorper, felis quam aliquam orci, ut pulvinar sapien.</p>
<div class="abs stat-num" style="left:611px;top:1068px">14</div>
<div class="abs stat-label" style="left:692px;top:1080px">Years of<br>experience</div>
<div class="abs stat-num" style="left:848px;top:1068px">187</div>
<div class="abs stat-label" style="left:962px;top:1080px">Projects<br>completed</div>

<div class="abs band"></div>

<div class="service active" style="left:114px">
  <svg viewBox="0 0 52 52"><path d="M26 6l18 9v22l-18 9-18-9V15z M8 15l18 9 18-9 M26 24v22 M17 10.5l18 9" fill="none" stroke="#fff" stroke-width="2"/></svg>
  <h3>Product<br>Design</h3><p>124 projects</p>
</div>
<div class="service" style="left:448px">
  <svg viewBox="0 0 52 52"><rect x="5" y="8" width="42" height="28" rx="2" fill="none" stroke="#6B429C" stroke-width="2"/><path d="M18 44h16M26 36v8" stroke="#6B429C" stroke-width="2"/><circle cx="22" cy="22" r="7" fill="none" stroke="#6C8BE0" stroke-width="2"/><path d="M33 16v12M37 19v9M41 22v6" stroke="#6C8BE0" stroke-width="2"/></svg>
  <h3>Full Stack<br>Develop</h3><p>37 projects</p>
</div>
<div class="service" style="left:780px">
  <svg viewBox="0 0 52 52"><path d="M26 8l10 18-10 18-10-18z" fill="none" stroke="#6B429C" stroke-width="2"/><circle cx="26" cy="26" r="3" fill="none" stroke="#6C8BE0" stroke-width="2"/><circle cx="8" cy="12" r="3" fill="none" stroke="#6C8BE0" stroke-width="2"/><circle cx="44" cy="12" r="3" fill="none" stroke="#6C8BE0" stroke-width="2"/><path d="M11 12h30" stroke="#6B429C" stroke-width="1.6"/></svg>
  <h3>Branding<br>Design</h3><p>62 projects</p>
</div>

<!-- ABOUT -->
<div class="abs" style="left:579px;top:1591px;width:314px;height:314px;border-radius:50%;background:var(--lilac-soft);opacity:.7"></div>
<div class="abs" style="left:889px;top:1573px;width:68px;height:68px;border-radius:50%;background:var(--lilac-soft)"></div>
<div class="photo" role="img" aria-label="Photo of a smiling woman with arms crossed in a striped sweater" style="left:137px;top:1610px;width:433px;height:639px;background:linear-gradient(180deg,#2a2220 0%,#6b4a3c 35%,#c94f86 65%,#5a4a3a 100%);border-radius:210px 210px 0 0"></div>
<h2 class="abs display sec-title" style="left:644px;top:1712px">About me</h2>
<p class="abs" style="left:644px;top:1790px;width:440px;font-size:13px;line-height:28px;font-weight:600;color:#555">Interdum et malesuada fames ac ante ipsum primis in faucibus. Donec ut suscipit purus. Praesent feugiat, magna sed ultricies ullamcorper, felis quam aliquam orci, ut pulvinar sapien.</p>
<p class="abs" style="left:644px;top:1892px;width:440px;font-size:13px;line-height:28px">Sed sollicitudin, enim ut pharetra consequat, nulla metus molestie est, in placerat lorem mi vel elit. In tincidunt, diam vel convallis congue, ante lorem porta odio, consectetur gravida risus lectus nec ipsum. Integer pharetra mauris quis augue rhoncus luctus. Integer semper elit in lacus viverra.</p>
<div class="btn btn-purple" style="left:644px;top:2068px;width:171px;height:47px">Learn more
  <svg viewBox="0 0 26 10"><path d="M2 5h20M18 1l4 4-4 4" stroke="#fff" stroke-width="1.6" fill="none"/></svg>
</div>

<!-- PROJECTS -->
<h2 class="abs display sec-title" style="left:114px;top:2356px">Creative projects</h2>
<div class="btn btn-purple" style="left:915px;top:2367px;width:171px;height:45px">Portfolio
  <svg viewBox="0 0 26 10"><path d="M2 5h20M18 1l4 4-4 4" stroke="#fff" stroke-width="1.6" fill="none"/></svg>
</div>
<p class="abs" style="left:114px;top:2436px;width:680px;font-size:13px;line-height:28px">Cras accumsan enim et ornare pharetra. Suspendisse consequat dolor ac dolor efficitur tempor. Proin a nisl vitae velit vestibulum blandit ac at dui. Phasellus sapien massa semper in neque eu, ornare tempus leo. Phasellus sit amet elit in sapien.</p>

<div class="project" style="left:114px;top:2612px;width:314px">
  <div class="shot" role="img" aria-label="Website screenshot of a kitchen and bath remodeling company" style="height:344px;background:linear-gradient(180deg,#dfe3e8 0%,#f5f5f5 45%,#ffffff 60%,#e9e2dc 100%)"></div>
  <div class="project-name" style="top:385px">Birch Remodeling</div>
</div>
<div class="project" style="left:454px;top:2567px;width:314px">
  <div class="shot" role="img" aria-label="Website screenshot of an insulation contractor" style="height:336px;background:linear-gradient(180deg,#3c4552 0%,#5a616b 45%,#d8c6b4 70%,#efe7de 100%)"></div>
  <div class="project-name" style="top:373px">Corvane Insulation</div>
</div>
<div class="project" style="left:795px;top:2620px;width:315px">
  <div class="shot" role="img" aria-label="Website screenshot of a patio contractor" style="height:336px;background:linear-gradient(180deg,#3b4048 0%,#7a5c46 38%,#ffffff 52%,#f3f3f3 100%)"></div>
  <div class="project-name" style="top:379px">Hollis Patios</div>
</div>
<div class="project" style="left:1139px;top:2567px;width:315px">
  <div class="shot" role="img" aria-label="Website screenshot of a roofing company" style="height:360px;background:linear-gradient(180deg,#22324a 0%,#3b4c66 30%,#ffffff 55%,#eeeeee 100%)"></div>
  <div class="project-name" style="top:360px">Dunmore Roofing</div>
</div>

<div class="abs slider-track"></div>
<div class="abs slider-fill"></div>
<div class="slider-arrow" style="left:980px"><svg width="8" height="14" viewBox="0 0 8 14"><path d="M7 1L1 7l6 6" stroke="#cfcfcf" stroke-width="1.6" fill="none"/></svg></div>
<div class="slider-arrow" style="left:1039px"><svg width="8" height="14" viewBox="0 0 8 14"><path d="M1 1l6 6-6 6" stroke="#6C8BE0" stroke-width="1.6" fill="none"/></svg></div>

<!-- RESUME -->
<div class="abs resume-bg"></div>
<div class="abs resume-side"></div>
<div class="abs avatar" role="img" aria-label="Portrait photo of a woman against a blue backdrop"></div>
<h2 class="abs display sec-title" style="left:503px;top:3320px">Resume</h2>
<p class="abs" style="left:503px;top:3398px;width:570px;font-size:13px;line-height:28px">I design and develop services for customers of all sizes, specializing in creating stylish, modern websites, web services and online stores. My passion is to design digital user experiences through the bold interface. Check out my Portfolio.</p>

<div class="info-label" style="left:503px;top:3518px">BIRTHDAY</div><div class="info-value" style="left:623px;top:3516px">4th April 1991</div>
<div class="info-label" style="left:503px;top:3559px">AGE</div><div class="info-value" style="left:623px;top:3557px">26 Yr</div>
<div class="info-label" style="left:503px;top:3600px">RESIDENCE</div><div class="info-value" style="left:623px;top:3598px">Canada</div>
<div class="info-label" style="left:503px;top:3640px">ADDRESS</div><div class="info-value" style="left:623px;top:3638px">California, USA</div>
<div class="info-label" style="left:835px;top:3518px">E-MAIL</div><div class="info-value" style="left:949px;top:3516px">info@verellnadia.co</div>
<div class="info-label" style="left:835px;top:3559px">PHONE</div><div class="info-value" style="left:949px;top:3557px">+044 318 2040</div>
<div class="info-label" style="left:835px;top:3600px">CHAT</div><div class="info-value" style="left:949px;top:3598px">chat.2718</div>
<div class="info-label" style="left:835px;top:3640px">FREELANCE</div><div class="info-value" style="left:949px;top:3638px">Available</div>

<div class="info-label" style="left:503px;top:3692px">INTERESTS</div>
<span class="tag" style="left:503px;top:3724px">Design</span>
<span class="tag" style="left:595px;top:3724px">UI/UX</span>
<span class="tag" style="left:675px;top:3724px">Responsive</span>
<span class="tag" style="left:781px;top:3724px">Development</span>
<span class="tag" style="left:895px;top:3724px">Branding</span>
<span class="tag" style="left:503px;top:3757px">Infographics</span>
<span class="tag" style="left:613px;top:3757px">Bootstrap</span>

<div class="btn btn-purple" style="left:503px;top:3826px;width:173px;height:45px">Full resume
  <svg viewBox="0 0 26 10"><path d="M2 5h20M18 1l4 4-4 4" stroke="#fff" stroke-width="1.6" fill="none"/></svg>
</div>

<!-- BLOG -->
<h2 class="abs display sec-title" style="left:0;top:4040px;width:1200px;text-align:center">Latet from blog</h2>
<svg class="blog-arrow" style="left:74px" width="10" height="18" viewBox="0 0 10 18"><path d="M9 1L1 9l8 8" stroke="#555" stroke-width="1.6" fill="none"/></svg>
<svg class="blog-arrow" style="left:1113px" width="10" height="18" viewBox="0 0 10 18"><path d="M1 1l8 8-8 8" stroke="#555" stroke-width="1.6" fill="none"/></svg>

<div class="photo" role="img" aria-label="Photo of hands typing on a laptop" style="left:114px;top:4144px;width:304px;height:275px;background:linear-gradient(135deg,#6e6e6e 0%,#b9b9b9 45%,#e6e6e6 100%)"></div>
<div class="blog-date" style="left:114px;top:4444px">29 SEPTEMBER, 2020</div>
<div class="blog-title" style="left:114px;top:4470px;width:310px">Aliquam cursus tortor neque, a gravida neque gravida</div>
<div class="read-more" style="left:116px;top:4546px">READ MORE</div>

<div class="blog-date" style="left:446px;top:4145px">29 SEPTEMBER, 2020</div>
<div class="blog-title" style="left:446px;top:4172px;width:310px">Nam quis quam risus ellent sed esque at mauris eget diam venenatis suscipit...</div>
<p class="abs" style="left:446px;top:4268px;width:310px;font-size:12.5px;line-height:27.5px">Fusce eu enim at nisl dapibus congue. Donec at urna rutrum, luctus velit non, ornare metus. Ut interdum et nisl in tempus. Donec vestibulum odio eu nisl malesuada, nec consequat sem tem por. Aliquam volutpat facilisis efficitur. Ut eget consequat quam, eu posuere augue. Vestibulum rhoncus dui ipsum, sed vulputate magna vehicula nec. Sed ut pulvinar mi. Suspendisse nec nunc sem. In interdum nisl dolor.</p>
<div class="read-more" style="left:448px;top:4546px">READ MORE</div>

<div class="photo" role="img" aria-label="Photo of a desk with a notebook, keyboard, glasses and coffee cup on a yellow surface" style="left:780px;top:4144px;width:304px;height:275px;background:linear-gradient(135deg,#f2c14e 0%,#f6cf63 50%,#e3b23f 100%)"></div>
<div class="blog-date" style="left:780px;top:4444px">29 SEPTEMBER, 2020</div>
<div class="blog-title" style="left:780px;top:4470px;width:310px">Aliquam cursus tortor neque, a gravida neque gravida</div>
<div class="read-more" style="left:782px;top:4546px">READ MORE</div>

<!-- FOOTER -->
<footer class="abs footer"></footer>
<div class="logo" style="left:112px;top:4750px">Nadia Verell</div>
<p class="abs" style="left:112px;top:4810px;font-size:12px;line-height:22px;color:var(--footer-text)">742 Alder Brook Rd. Suite 310<br>Fairhaven, IL 60412</p>
<div class="foot-icon" style="left:112px;top:4866px"><svg width="12" height="10" viewBox="0 0 12 10"><rect x="1" y="1" width="10" height="8" fill="none" stroke="#fff" stroke-width="1.2"/><path d="M1 1l5 4 5-4" stroke="#fff" stroke-width="1.2" fill="none"/></svg></div>
<div class="foot-link" style="left:150px;top:4869px">info@verellnadia.co</div>
<div class="foot-icon" style="left:112px;top:4904px"><svg width="12" height="12" viewBox="0 0 12 12"><path d="M2 1h2.5l1 3-1.5 1a7 7 0 003 3l1-1.5 3 1V10a1 1 0 01-1 1A9 9 0 011 2a1 1 0 011-1z" fill="#fff"/></svg></div>
<div class="foot-link" style="left:150px;top:4907px">+044 318 2040</div>

<div class="foot-head" style="left:444px;top:4750px">About</div>
<div class="foot-link" style="left:444px;top:4798px">Home</div>
<div class="foot-link" style="left:444px;top:4828px">About me</div>
<div class="foot-link" style="left:444px;top:4857px">Portfolio</div>
<div class="foot-link" style="left:444px;top:4888px">Blog</div>
<div class="foot-link" style="left:444px;top:4918px">Resume</div>

<div class="foot-head" style="left:642px;top:4750px">Left</div>
<div class="foot-link" style="left:642px;top:4798px">Sitemap</div>
<div class="foot-link" style="left:642px;top:4828px">Imprint</div>
<div class="foot-link" style="left:642px;top:4857px">Terms and conditions</div>
<div class="foot-link" style="left:642px;top:4888px">Privacy policy</div>

<div class="foot-head" style="left:833px;top:4750px">Newsletters</div>
<div class="foot-link" style="left:833px;top:4794px;font-size:12px">Signup below to join our mailing list</div>
<div class="abs newsletter-input">Email address</div>
<div class="abs newsletter-btn">SUBSCRIBE NOW</div>

<div class="abs foot-rule"></div>
<div class="foot-link" style="left:112px;top:5026px;font-size:11px">© 2021 Nadia Verell . All rights reserved</div>
<span class="social-dot" style="left:938px"></span>
<span class="social-dot" style="left:977px"></span>
<span class="social-dot" style="left:1016px"></span>
<span class="social-dot" style="left:1055px"></span>

</body>
</html>
```